Oru Loft Business Card

We need a business card designed for a a company called "Oru Loft". We offer consulting, coaching and training to business leaders and coaches (across the world) using the latest findings in neuroscience, social and emotional intelligence and positive psychology. The final design should communicate the use of brain science to create sustainable relationships.

The card should be doublesided. The logo is attached and names and titles will be provided to the successful designer. Thank you.

```html
<!DOCTYPE html>
<html lang="en">
<head>
<meta charset="utf-8">
<title>Oru Loft Business Card</title>
<link rel="stylesheet" href="https://fonts.googleapis.com/css2?family=Arimo:wght@400;500;700&display=swap">
<style>
  :root {
    --page: #ffffff;
    --card-dark: #1b1b1b;
    --card-light: #ffffff;
    --card-edge: #d9d9d9;
    --ink: #1b1b1b;
    --brand-blue: #2894f0;
    --brand-lime: #b5ff00;
  }
  html, body {
    margin: 0;
    padding: 0;
    width: 1200px;
    height: 1000px;
    overflow: hidden;
    background: var(--page);
    font-family: "Arimo", Helvetica, Arial, sans-serif;
    color: var(--ink);
  }
  .canvas {
    position: relative;
    width: 1200px;
    height: 1000px;
  }
  .card {
    position: absolute;
    left: 239px;
    width: 724px;
    height: 433px;
    box-sizing: border-box;
    overflow: hidden;
  }
  .card--front {
    top: 48px;
    background: var(--card-dark);
    display: flex;
    align-items: center;
    justify-content: center;
  }
  .brand {
    display: flex;
    align-items: center;
    gap: 14px;
    margin-top: 10px;
  }
  .brand__square {
    width: 30px;
    height: 30px;
    background: var(--brand-lime);
  }
  .brand__name {
    font-weight: 700;
    font-size: 50px;
    letter-spacing: 1px;
    color: var(--brand-blue);
    line-height: 1;
  }
  .card--back {
    top: 521px;
    height: 433px;
    background: var(--card-light);
    border: 1px solid var(--card-edge);
  }
  .person {
    position: absolute;
    left: 28px;
    top: 44px;
  }
  .person__name {
    margin: 0;
    font-size: 24px;
    font-weight: 500;
    line-height: 30px;
  }
  .person__title {
    margin: 0;
    font-size: 19px;
    line-height: 22px;
  }
  .contact {
    position: absolute;
    left: 27px;
    top: 236px;
    margin: 0;
    padding: 0;
    list-style: none;
    font-size: 19px;
    line-height: 26.7px;
  }
  .back-art {
    position: absolute;
    right: 0;
    top: 0;
    width: 170px;
    height: 433px;
  }
</style>
</head>
<body>
  <main class="canvas">
    <section class="card card--front" aria-label="Card front">
      <div class="brand">
        <span class="brand__square" aria-hidden="true"></span>
        <span class="brand__name">Oru Loft</span>
      </div>
    </section>

    <section class="card card--back" aria-label="Card back">
      <div class="person">
        <h1 class="person__name">Firtsname Lastname</h1>
        <p class="person__title">Title</p>
      </div>
      <ul class="contact">
        <li>email@email.com</li>
        <li>office: 000.000.0000</li>
        <li>mobile: 000.000.0000</li>
        <li>address line 1</li>
        <li>address line 2</li>
        <li>www.domain.com</li>
      </ul>
      <svg class="back-art" role="img" aria-label="Large dark brand symbol decoration on the right edge" viewBox="0 0 170 433" preserveAspectRatio="none">
        <rect x="0" y="0" width="170" height="433" fill="var(--card-dark)"/>
      </svg>
    </section>
  </main>
</body>
</html>
```